Banner Ad Design Project

Process description of accounting delivery A to Z

Your folder appointment for delivery of receipts, in and outgoing invoices not necessary but possible – goes into a industrial sized scanner at the office

Electronic delivery via email, CloudVault or remote scanning locally at the clients office

Imported into the accounting software (called Sheetfree) with drag and drop from email and CloudVault our directly imported from scanner at clients office

Software sets ledger accounts after scanning largely automated
Imported into accounting softer and finished by producing Income statement , Balance sheet and cash flow statements.

Size should fit the www.fennivar.no webpage banners rolling

Target Market(s)

New Clients - its to sell our work as modern

Industry/Entity Type

Accounting

Requirements
Must have
• Color scheme fitting current webpage. Looking for a process driven illustration where details are more 1D not 3D as such. Simplified and easy to grasp scheme of flow in our production pipeline.

```html
<!DOCTYPE html>
<html lang="en">
<head>
<meta charset="utf-8">
<title>Delivery Process Banners</title>
<link rel="stylesheet" href="https://fonts.googleapis.com/css2?family=Gochi+Hand&family=Indie+Flower&display=swap">
<style>
  :root {
    --green: #1f8a67;
    --green-dark: #17714f;
    --pink: #e2306c;
    --ink: #5a5a5a;
    --paper: #ebebea;
    --paper-light: #f6f6f4;
    --frame: #1e1e1e;
    --white: #ffffff;
    --steel: #a3a6a6;
    --lid: #5b5b5b;
  }
  html, body {
    margin: 0;
    width: 1200px;
    height: 960px;
    overflow: hidden;
    background: var(--frame);
  }
  .canvas {
    position: relative;
    width: 1200px;
    height: 960px;
    background: var(--frame);
  }
  .banner {
    position: absolute;
    left: 0;
    width: 1200px;
    height: 452px;
    background: var(--paper);
    overflow: hidden;
  }
  .banner--english { top: 12px; }
  .banner--norwegian { top: 478px; }
  .banner svg { display: block; }

  .stage-heading {
    font-family: "Gochi Hand", cursive;
    font-size: 31px;
    fill: var(--green);
    letter-spacing: 0.5px;
  }
  .label {
    font-family: "Indie Flower", cursive;
    font-size: 15px;
    fill: var(--ink);
  }
  .label--white { fill: var(--white); }
  .label--small { font-size: 13px; }
  .band { fill: var(--green); }
  .band-title {
    font-family: "Gochi Hand", cursive;
    font-size: 34px;
    fill: var(--white);
    letter-spacing: 1px;
  }

  .arrow {
    fill: none;
    stroke: var(--pink);
    stroke-width: 2.4;
    stroke-linejoin: round;
    stroke-linecap: round;
  }
  .fill-green { fill: var(--green); }
  .fill-dark { fill: var(--green-dark); }
  .fill-lid { fill: var(--lid); }
  .outline-green { fill: var(--paper-light); stroke: var(--green); stroke-width: 3; stroke-linejoin: round; }
  .line-white { fill: none; stroke: var(--white); stroke-width: 1.8; stroke-linejoin: round; }
  .line-grey { fill: var(--white); stroke: var(--ink); stroke-width: 1.4; stroke-linejoin: round; }
  .bar-grey { fill: #a9a9a9; }
  .bar-green { fill: var(--green); opacity: 0.55; }
  .lens { fill: rgba(255,255,255,0.55); stroke: var(--steel); stroke-width: 5; }
  .lens-handle { stroke: var(--steel); stroke-width: 8; stroke-linecap: round; }
</style>
</head>
<body>
<main class="canvas">

  <section class="banner banner--english" aria-label="Standard and Electronic Delivery Process">
    <svg width="1200" height="452" viewBox="0 0 1200 452">
      <text class="stage-heading" x="188" y="44">Delivery</text>
      <text class="stage-heading" x="594" y="34">Processing</text>
      <text class="stage-heading" x="960" y="40">Finalisation</text>

      <g class="icon-folder" role="img" aria-label="Folder of vouchers">
        <path class="outline-green" d="M58 244 L58 328 L184 328 L184 248 L152 248 L145 236 L112 236 L106 244 Z"/>
        <path class="fill-green" d="M52 252 L62 248 L64 330 L54 332 Z"/>
        <text class="label" x="121" y="296" text-anchor="middle">Voucher(s)</text>
      </g>
      <polygon class="arrow" points="228,288 264,288 264,280 282,294 264,308 264,300 228,300"/>

      <text class="label" x="308" y="140">Email/CloudVault</text>
      <g class="icon-mail-cloud" role="img" aria-label="Email envelope and cloud storage">
        <rect class="line-grey" x="358" y="161" width="24" height="18"/>
        <path fill="none" stroke="#5a5a5a" stroke-width="1.4" d="M358 161 L370 172 L382 161"/>
        <path class="fill-green" d="M384 184 Q378 184 379 177 Q381 171 387 173 Q389 164 398 166 Q405 168 405 175 Q411 176 410 181 Q409 184 404 184 Z"/>
      </g>
      <path class="arrow" d="M378 226 Q370 214 380 204 M380 204 l-1 7 M392 204 Q400 216 390 226 M390 226 l1 -7"/>

      <g class="icon-scanner" role="img" aria-label="Document scanner">
        <path class="fill-lid" d="M346 240 L422 240 L428 256 L340 256 Z"/>
        <rect class="fill-green" x="336" y="256" width="96" height="72" rx="3"/>
        <rect class="line-white" x="346" y="262" width="76" height="42"/>
        <rect class="fill-dark" x="352" y="267" width="64" height="32"/>
        <text class="label label--white label--small" x="384" y="322" text-anchor="middle">Scan</text>
      </g>
      <polygon class="arrow" points="539,312 539,262 529,262 545,238 561,262 551,262 551,312"/>

      <g class="icon-monitor" role="img" aria-label="Computer monitor running the Sheetfree accounting software">
        <rect class="fill-green" x="468" y="60" width="146" height="90" rx="3"/>
        <rect class="line-white" x="476" y="68" width="130" height="74"/>
        <circle class="line-white" cx="500" cy="105" r="15"/>
        <ellipse class="line-white" cx="500" cy="105" rx="6" ry="15"/>
        <path class="line-white" d="M485 105 H515 M488 97 H512 M488 113 H512"/>
        <text class="label label--white" x="562" y="110" text-anchor="middle" style="font-size:17px">Sheetfree</text>
        <rect class="fill-green" x="533" y="150" width="16" height="9"/>
        <rect class="fill-green" x="498" y="159" width="86" height="5" rx="2"/>
      </g>
      <polygon class="arrow" points="642,118 678,118 678,110 696,124 678,138 678,130 642,130"/>

      <g class="icon-desk" role="img" aria-label="Accounting desk with computer">
        <rect class="line-grey" x="804" y="76" width="28" height="19"/>
        <rect fill="#5a5a5a" x="815" y="95" width="6" height="5"/>
        <rect class="fill-green" x="730" y="100" width="112" height="10"/>
        <rect class="fill-green" x="736" y="110" width="9" height="60"/>
        <rect class="fill-green" x="790" y="110" width="48" height="60"/>
        <path class="line-white" d="M796 128 H832 M796 148 H832 M810 120 H818 M810 140 H818 M810 160 H818"/>
      </g>
      <text class="label" x="847" y="122">Processing</text>
      <polygon class="arrow" points="768,160 780,160 780,190 788,190 774,210 760,190 768,190"/>

      <text class="label" x="648" y="294">Electronic</text>
      <text class="label" x="648" y="311">Archiving</text>
      <g class="icon-archive" role="img" aria-label="Electronic archive disk">
        <path class="fill-green" d="M742 234 L818 234 L830 246 L830 328 L742 328 Z"/>
        <rect class="line-white" x="756" y="244" width="60" height="76"/>
        <polygon class="line-white" points="781,270 791,270 791,290 798,290 786,304 774,290 781,290"/>
      </g>
      <polygon class="arrow" points="854,309 948,309 948,302 966,313 948,324 948,317 854,317"/>

      <g class="icon-report" role="img" aria-label="Annual report under a magnifying glass">
        <rect class="outline-green" x="986" y="236" width="86" height="94" style="fill:#fff"/>
        <rect class="bar-grey" x="994" y="244" width="64" height="5"/>
        <rect class="bar-grey" x="994" y="254" width="46" height="4"/>
        <text class="label label--small" x="990" y="294">Annual</text>
        <text class="label label--small" x="990" y="309">report</text>
        <line class="lens-handle" x1="1074" y1="330" x2="1094" y2="354"/>
        <circle class="lens" cx="1060" cy="316" r="18"/>
      </g>

      <path class="band" d="M240 386 Q600 378 962 384 L968 446 Q600 440 250 446 L264 416 Z"/>
      <text class="band-title" x="608" y="428" text-anchor="middle">Standard and Electronic Delivery Process</text>
    </svg>
  </section>

  <section class="banner banner--norwegian" aria-label="Standard og Elektronisk leveringsprosess" lang="no">
    <svg width="1200" height="452" viewBox="0 0 1200 452">
      <text class="stage-heading" x="188" y="44">Levere</text>
      <text class="stage-heading" x="594" y="34">Behandle</text>
      <text class="stage-heading" x="946" y="40">Ferdigstille</text>

      <g class="icon-folder" role="img" aria-label="Mappe med bilag">
        <path class="outline-green" d="M58 244 L58 328 L184 328 L184 248 L152 248 L145 236 L112 236 L106 244 Z"/>
        <path class="fill-green" d="M52 252 L62 248 L64 330 L54 332 Z"/>
        <text class="label" x="121" y="296" text-anchor="middle">Bilag</text>
      </g>
      <polygon class="arrow" points="228,288 264,288 264,280 282,294 264,308 264,300 228,300"/>

      <text class="label" x="308" y="140">Email/CloudVault</text>
      <g class="icon-mail-cloud" role="img" aria-label="E-post og skylagring">
        <rect class="line-grey" x="358" y="161" width="24" height="18"/>
        <path fill="none" stroke="#5a5a5a" stroke-width="1.4" d="M358 161 L370 172 L382 161"/>
        <path class="fill-green" d="M384 184 Q378 184 379 177 Q381 171 387 173 Q389 164 398 166 Q405 168 405 175 Q411 176 410 181 Q409 184 404 184 Z"/>
      </g>
      <path class="arrow" d="M378 226 Q370 214 380 204 M380 204 l-1 7 M392 204 Q400 216 390 226 M390 226 l1 -7"/>

      <g class="icon-scanner" role="img" aria-label="Skanner">
        <path class="fill-lid" d="M346 240 L422 240 L428 256 L340 256 Z"/>
        <rect class="fill-green" x="336" y="256" width="96" height="72" rx="3"/>
        <rect class="line-white" x="346" y="262" width="76" height="42"/>
        <rect class="fill-dark" x="352" y="267" width="64" height="32"/>
        <text class="label label--white label--small" x="384" y="322" text-anchor="middle">Skanner</text>
      </g>
      <polygon class="arrow" points="539,312 539,262 529,262 545,238 561,262 551,262 551,312"/>

      <g class="icon-monitor" role="img" aria-label="Skjerm med regnskapsprogrammet Sheetfree">
        <rect class="fill-green" x="468" y="60" width="146" height="90" rx="3"/>
        <rect class="line-white" x="476" y="68" width="130" height="74"/>
        <circle class="line-white" cx="500" cy="105" r="15"/>
        <ellipse class="line-white" cx="500" cy="105" rx="6" ry="15"/>
        <path class="line-white" d="M485 105 H515 M488 97 H512 M488 113 H512"/>
        <text class="label label--white" x="562" y="110" text-anchor="middle" style="font-size:17px">Sheetfree</text>
        <rect class="fill-green" x="533" y="150" width="16" height="9"/>
        <rect class="fill-green" x="498" y="159" width="86" height="5" rx="2"/>
      </g>
      <polygon class="arrow" points="642,118 678,118 678,110 696,124 678,138 678,130 642,130"/>

      <g class="icon-desk" role="img" aria-label="Skrivebord for bokføring">
        <rect class="line-grey" x="804" y="76" width="28" height="19"/>
        <rect fill="#5a5a5a" x="815" y="95" width="6" height="5"/>
        <rect class="fill-green" x="730" y="100" width="112" height="10"/>
        <rect class="fill-green" x="736" y="110" width="9" height="60"/>
        <rect class="fill-green" x="790" y="110" width="48" height="60"/>
        <path class="line-white" d="M796 128 H832 M796 148 H832 M810 120 H818 M810 140 H818 M810 160 H818"/>
      </g>
      <text class="label" x="847" y="122">Bokføring</text>
      <polygon class="arrow" points="768,160 780,160 780,190 788,190 774,210 760,190 768,190"/>

      <text class="label" x="642" y="288">Elektronisk</text>
      <text class="label" x="642" y="305">Arkiv</text>
      <g class="icon-archive" role="img" aria-label="Elektronisk arkiv">
        <path class="fill-green" d="M742 234 L818 234 L830 246 L830 328 L742 328 Z"/>
        <rect class="line-white" x="756" y="244" width="60" height="76"/>
        <polygon class="line-white" points="781,270 791,270 791,290 798,290 786,304 774,290 781,290"/>
      </g>
      <polygon class="arrow" points="854,309 948,309 948,302 966,313 948,324 948,317 854,317"/>

      <g class="icon-report" role="img" aria-label="Årsregnskap under forstørrelsesglass">
        <rect class="outline-green" x="986" y="236" width="86" height="94" style="fill:#fff"/>
        <rect class="bar-grey" x="994" y="244" width="64" height="5"/>
        <rect class="bar-grey" x="994" y="254" width="46" height="4"/>
        <text class="label label--small" x="990" y="282">Årsregnskap</text>
        <line class="lens-handle" x1="1074" y1="330" x2="1094" y2="354"/>
        <circle class="lens" cx="1060" cy="316" r="18"/>
      </g>

      <path class="band" d="M240 386 Q600 378 962 384 L968 446 Q600 440 250 446 L264 416 Z"/>
      <text class="band-title" x="608" y="428" text-anchor="middle">Standard og Elektronisk - leveringsprosess</text>
    </svg>
  </section>

</main>
</body>
</html>
```